Tradeshow Booth, Banners & Brochure Design

Corvi Lattice (www.corvilattice-example.com) is a Nortwell Affiliate specializing in developing products and customizations for Nortwell Ledgerline KX. The purpose of this project is to develop a unified approach to graphic design for our tradeshow booth, banners and product literature. This should result in completed designs for the booth and banners, and several templates that can be used to create our product literature.

***WE WILL ONLY LOOK THROUGH THE FIRST 100 SUBMISSIONS***

Reason: We have received some requests for an extended deadline, and we would like to encourage more submissions, so we are extending the deadline by two days. Please let us know if you have any questions or need clarification on our design brief.

Thanks for the submissions and questions everyone.  I will get answers to your questions, and more detailed specs, posted within the next couple of hours.  I will also provide detailed feedback to your designs within that time.

Q:  How large should each item be – what is the approximate number of words/lines, columns/rows?

 

-          We have updated the Content Type list to cut it down and simplify this.  For word count, we are attaching the text for our NEW brochure on WMS, which we intend to be a 4 page brochure.  We have labeled each section according to content type.  This can be used as a guide for how much text each content area must be able to accommodate.  You can even pull the raw text straight from the word file for your design.  The RVOT brochure, already included, is an OLD brochure, and represents a design that we are trying to evolve beyond.

 

-          Keep in mind that the 4 page product brochure will be a 17” by 11” single sheet, folded.  The 2 page product brochure will be a single 8.5” by 11” sheet, printed on both sides.

 

-          For the 2 page product brochure, assume something that looks like half of the 4 page design.  For example, we will be creating one brochure for “Financials” which comprises two products.  Product A will go on the front, and Product B on the back.  We will still need to allow for contact information and the other content types as specified.

 

-          For the 4 page corporate overview, we have attached our current corporate overview for reference, and labeled the content types.  Again, feel free to pull raw text directly from this for purposes of your design – though remember, this OLD brochure represents a design we are trying to evolve beyond.

 

-          For images (screenshots, stock photography, diagrams, etc) we are thinking we would like to see about 4 on the 4 page brochure, but only 1-2 for the 2 page brochure.  The corporate overview can have suitable imagery at your discretion.

 

-          We would like to see some of the imagery used in the Tradeshow materials (booth, banners) carried across to the brochures.

 

 

 

Q:  What are the detailed print guidelines, especially in relation to bleeds, etc?

 

-          For all the brochures, use a full bleed.  If your design incorporates a bleed of color across a fold, try to have the bleed going across no more than 25% of the height of the page.  CMYK color, 300DPI, 8.5”w x 11”h.  We will most likely go with 100# paper without too much gloss on it. 

 

-          For all other materials such as booth and banners, no bleeds.  Please see specification sheets for the booth and banners, included below.  Create your designs to the exact size given.

 

 

 

Q:  Will booth graphics be printed as one continuous piece, or will they be applied in sections that are in line with the panel dimensions of the 8 center panels and end caps?

 

-          Graphics are printed as one continuous piece on a large format printer.  They are then cut into the individual panel pieces for shipping and storage.  When the booth is fully assembled, the seams are hardly noticeable unless you are looking for them from a short distance away.

 

-          We are already in possession of one 10’ booth, and will be ordering another, with the associated pieces, to create the 20’ booth.  The booth comprises a support structure, and the actual graphics panels which are attached to the front.  The overall 20’ design should take into account the fact that we will, in the future, attend tradeshows with only a 10’ booth, so only half of the panels will be used.  We would like to be able to mix and match our four categories to suit the show.

Reason: We are extending the deadline one more time to allow Tamsin and anyone else who needs the extra time for the brochure design.

Please prioritize your brochure design at this time.  We are interested in receiving feedback on deadlines - if you can confirm that you will submit a design but need more time to do so, we would like to hear from you.

Reason: To provide time for solid designs from all the designers who have been invited, we are extended the deadline one more time. This will be the final extension.

Target Market(s)

Corporate Clients

Industry/Entity Type

Graphic Design

Requirements
Must have
• TRADESHOW SPECIFIC
1. Graphics for 10'x20' “Gullwing” Tradeshow Booth
a. Layout should approximate the grid we have mocked up in our preliminary layout – see below. There is a fair amount of flexibility so long as the basic grid, contents and dimensions are adhered to.

2. Graphics needed for 3 retractable banner stands
a. Two banner stands will have dimensions of 24” x 88”
b. The third banner stand will have dimensions of 36” x 88” and will be double-sided. The design for this banner should have the option to be scaled down to 33.5” wide, for a possible additional banner stand being considered.
c. Banners should approximate what is shown in the preliminary layout – see below.
d. All banner stands being used are able to fully extend to 92”- however, the height of the booth itself is 88” and we would like all tradeshow specific elements to be the same height.

PRODUCT LITERATURE
1. Graphic Design and Layout needed for brochures:
a. double-sided one page for Products
b. double-sided two page for Products
c. double-sided two page for Overview

2. Pages would be full bleed letter size 8.5” x 11.

3. Samples are included below to get an idea of common grids and layouts for similar publications, as well as one of our current publications for reference.

4. Product literature must include provisions for all of the content types listed in that document, included below. There is some leeway with image placement – a product brochure doesn’t necessarily have to have stock photos, diagrams, AND software screenshots.

5. The designer will need to indicate what specs are required for software screenshots so that we can generate appropriate files for that use.

COMMON ELEMENTS
• Images need to include stock photos of people in business settings, as well as stock photos related to warehousing, barcoding systems, and supply chains. Other images to be used should include schematics, workflow diagrams, and other items that are related to the areas in which the company works. Each heading on the booth, and each page on the brochures, will need one image at minimum. Images and content laid out next to each other should be thematically related whenever possible. We will also create a small number of simple diagrams in house that will need to be redesigned and recreated in the appropriate format and placed in the designs.
• Clean, high-impact design. The Nortwell Quantive Bookkeeping brochure, included below, is a good example of this.
• Our current logo, included below, needs to have the tagline removed. We are also requesting that a different version of the graphic element in the logo be created, in monochrome but with roughly the same geometry.
• Our new tagline is “Integrated Solutions for Ledgerline KX” but it should not be located directly in the logo area as our current tagline is, “Making systems business-ready”.
• Designs should be produced in print-ready PDF files. We will be using Quillmark Layoutry V9 to open the PDF files, drop in our copy and other content, and finalize the designs. The PDF files will then be sent directly to our booth production and brochure printing companies.

```html
<!DOCTYPE html>
<html lang="en">
<head>
<meta charset="utf-8">
<title>Corvi Lattice – Retractable Banner Set</title>
<link rel="stylesheet" href="https://fonts.googleapis.com/css2?family=Dosis:wght@600;700&family=Roboto:wght@900&display=swap">
<style>
  :root {
    --page: #ffffff;
    --header: #ffffff;
    --violet: #6262a4;
    --title-grey: #6b6b6b;
    --brand-ink: #2b2b2b;
    --brand-mark: #8a8a8a;
    --divider: #dcdcdc;
    --facet-light: #d6d6d6;
    --facet-dark: #b3b3b3;
    --photo-warm: #b97a3c;
    --photo-blue: #4b55a8;
    --label: #ffffff;
  }
  * { box-sizing: border-box; margin: 0; padding: 0; }
  html, body { width: 1200px; height: 1200px; overflow: hidden; background: var(--page); }
  .canvas { position: relative; width: 1200px; height: 1200px; }

  .banner {
    position: absolute; top: 30px; width: 298px; height: 1140px;
    background: var(--violet); overflow: hidden;
    box-shadow: 0 1px 4px rgba(0,0,0,0.25);
  }
  .banner--list { left: 70px; }
  .banner--photo { left: 467px; }
  .banner--columns { left: 840px; }

  .banner__photo {
    position: absolute; left: 0; top: 200px; width: 100%; height: 940px;
    background: linear-gradient(160deg, var(--photo-warm) 0%, #8c6a4a 30%, var(--photo-blue) 55%, #c8955e 80%, #6f5a4a 100%);
  }

  .banner__header { position: absolute; left: 0; top: 0; width: 298px; height: 314px; }

  .brand {
    position: absolute; top: 36px; left: 0; width: 100%;
    display: flex; align-items: center; justify-content: center; gap: 10px;
  }
  .brand__square { width: 34px; height: 34px; background: var(--brand-mark); }
  .brand__name {
    font-family: "Dosis", sans-serif; font-weight: 700; font-size: 26px;
    color: var(--brand-ink); letter-spacing: 0.2px; text-transform: lowercase;
  }

  .tagline {
    position: absolute; top: 104px; left: 0; width: 100%; text-align: center;
    font-family: "Dosis", sans-serif; font-weight: 700; color: var(--title-grey);
    text-transform: uppercase;
  }
  .tagline__main { display: block; font-size: 43px; line-height: 46px; letter-spacing: 0.5px; }
  .tagline__sub { display: block; font-size: 22px; line-height: 30px; letter-spacing: 0.8px; margin-top: 2px; }

  .offerings {
    position: absolute; top: 350px; left: 0; width: 100%; list-style: none;
    font-family: "Roboto", sans-serif; font-weight: 900; color: var(--label);
    font-size: 21px; letter-spacing: 0.6px; text-align: center; text-transform: uppercase;
  }
  .offerings li { height: 57px; line-height: 28px; }

  .offerings--vertical { top: 318px; height: 324px; display: flex; justify-content: center; gap: 36px; }
  .offerings--vertical li {
    height: 324px; line-height: 30px; width: 30px;
    writing-mode: vertical-rl; transform: rotate(180deg); text-align: end;
  }

  .banner__base {
    position: absolute; left: 0; top: 668px; width: 100%; height: 472px;
    border-top: 16px solid var(--divider);
    background: linear-gradient(170deg, var(--facet-light) 0%, #c6c6c6 40%, var(--facet-dark) 70%, #cbcbcb 100%);
  }
</style>
</head>
<body>
<main class="canvas">

  <section class="banner banner--list">
    <svg class="banner__header" viewBox="0 0 298 314" aria-hidden="true">
      <polygon points="0,0 298,0 298,240 149,312 0,240" fill="var(--header)"/>
    </svg>
    <div class="brand"><span class="brand__square"></span><span class="brand__name">corvi lattice</span></div>
    <h2 class="tagline"><span class="tagline__main">Integrated<br>Solutions</span><span class="tagline__sub">for Ledgerline KX</span></h2>
    <ul class="offerings">
      <li>WMS/Distribution</li>
      <li>Workflow</li>
      <li>Customization</li>
      <li>Financials</li>
    </ul>
    <div class="banner__base" role="img" aria-label="Faint large faceted geometric decoration in light greys"></div>
  </section>

  <section class="banner banner--photo">
    <div class="banner__photo" role="img" aria-label="Photo of a warehouse worker in a blue coat carrying a cardboard box in front of shelving"></div>
    <svg class="banner__header" viewBox="0 0 298 314" aria-hidden="true">
      <polygon points="0,0 298,0 298,240 149,312 0,240" fill="var(--header)"/>
    </svg>
    <div class="brand"><span class="brand__square"></span><span class="brand__name">corvi lattice</span></div>
    <h2 class="tagline"><span class="tagline__main">Integrated<br>Solutions</span><span class="tagline__sub">for Ledgerline KX</span></h2>
  </section>

  <section class="banner banner--columns">
    <svg class="banner__header" viewBox="0 0 298 314" aria-hidden="true">
      <polygon points="0,0 298,0 298,240 149,312 0,240" fill="var(--header)"/>
    </svg>
    <div class="brand"><span class="brand__square"></span><span class="brand__name">corvi lattice</span></div>
    <h2 class="tagline"><span class="tagline__main">Integrated<br>Solutions</span><span class="tagline__sub">for Ledgerline KX</span></h2>
    <ul class="offerings offerings--vertical">
      <li>Financials</li>
      <li>Customization</li>
      <li>Workflow</li>
      <li>WMS/Distribution</li>
    </ul>
    <div class="banner__base" role="img" aria-label="Faint large faceted geometric decoration in light greys"></div>
  </section>

</main>
</body>
</html>
```